Silver Creek Plumbing Business card & letter head design

We need a new business card and letter head for our plumbing company called silver creek plumbing. attached is the companys logo. We provide domestic and commercial plumbing services in regional western Australia. We are after Something simple yet nice to look at and something that fits within the trade industry.

Target Market(s)

trade/building industry

Contact Information for Business Card

Darl Hensby
Manager
0461 238 574
enquiries@scplumbwork.net.au
ABN: 47 381 905 462
PCL: 5187

Domestic & Commercial Plumbing
Tip Truck & Excavator hire

Colors

Designer to choose colors to be used in the design.

```html
<!DOCTYPE html>
<html lang="en">
<head>
<meta charset="utf-8">
<title>Silver Creek Plumbing — Business Card &amp; Letterhead</title>
<link href="https://fonts.googleapis.com/css2?family=Lato:wght@400;700;900&family=Yellowtail&display=swap" rel="stylesheet">
<style>
  :root{
    --backdrop:#b5b6ba;
    --brand-blue:#0e58a3;
    --swoosh-grey:#58595b;
    --text-grey:#4a4a4a;
    --paper:#ffffff;
    --paper-shade:#efeff0;
    --white:#ffffff;
  }
  *{margin:0;padding:0;box-sizing:border-box}
  html,body{width:1200px;height:1045px;overflow:hidden}
  body{background:var(--backdrop);font-family:'Lato',sans-serif;position:relative}

  .wordmark{font-family:'Lato',sans-serif;font-weight:900;text-transform:uppercase;text-align:center;letter-spacing:.5px;line-height:1.05}

  /* Business card shared */
  .card{position:absolute;left:80px;width:308px;height:176px;border-radius:9px;overflow:hidden}
  .card-front{top:520px;background:linear-gradient(160deg,var(--paper) 30%,var(--paper-shade))}
  .card-back{top:725px;background:var(--brand-blue)}
  .card svg.wave{position:absolute;left:0;top:0}
  .card-front .wordmark{position:absolute;top:26px;left:0;width:100%;color:var(--brand-blue);font-size:19px}
  .card-holder{position:absolute;top:98px;width:100%;text-align:center;font-size:10px;font-weight:700;color:var(--brand-blue)}
  .card-holder .role{font-weight:400;font-size:8px;color:var(--text-grey);text-transform:uppercase}
  .card-contact{position:absolute;left:0;width:100%;text-align:center;color:var(--white);font-size:8px}
  .card-contact b{font-weight:700}
  .card-contact .sep{margin:0 6px}
  .line-1{top:143px}
  .line-2{top:157px}
  .icon{display:inline-block;vertical-align:-2px;margin-right:3px}
  .card-back .wordmark{position:absolute;top:50px;left:0;width:100%;color:var(--white);font-size:24px}
  .card-back .services{position:absolute;top:148px;width:100%;text-align:center;color:var(--white);font-size:8.5px}

  /* Letterhead */
  .letterhead{position:absolute;left:412px;top:73px;width:668px;height:864px;overflow:hidden;
    background:linear-gradient(160deg,var(--paper) 35%,var(--paper-shade))}
  .letterhead .wordmark{position:absolute;top:28px;left:0;width:100%;color:var(--brand-blue);font-size:26px}
  .letter-body{position:absolute;left:57px;top:225px;width:554px;color:var(--text-grey)}
  .salutation{color:var(--brand-blue);font-weight:700;font-size:13px;margin-bottom:14px}
  .letter-body p.para{font-size:13px;line-height:19.6px;text-align:justify;margin-bottom:15px}
  .closing{font-size:15px;margin-top:22px;color:#333}
  .signature{font-family:'Yellowtail',cursive;color:var(--brand-blue);font-size:26px;margin-top:4px}
  .letterhead svg.wave{position:absolute;left:0;top:0}
  .lh-footer{position:absolute;left:0;width:100%;text-align:center;color:var(--white);font-size:9.5px}
  .lh-footer .sep{margin:0 8px}
  .lh-footer b{font-weight:700}
  .lh-line-1{top:822px}
  .lh-line-2{top:839px}
</style>
</head>
<body>

  <!-- Business card, front -->
  <section class="card card-front">
    <svg class="wave" width="308" height="176" viewBox="0 0 308 176">
      <path d="M0 104 Q154 160 308 104 L308 176 L0 176 Z" fill="var(--brand-blue)"/>
      <path d="M0 86 Q110 134 250 124 Q120 128 0 96 Z" fill="var(--swoosh-grey)"/>
    </svg>
    <div class="wordmark">Silver Creek<br>Plumbing</div>
    <div class="card-holder">DARL HENSBY, <span class="role">Manager</span></div>
    <div class="card-contact line-1"><b>ABN:</b> 47 381 905 462<span class="sep">|</span><b>PCL:</b> 5187</div>
    <div class="card-contact line-2">
      <svg class="icon" width="8" height="8" viewBox="0 0 10 10"><circle cx="5" cy="5" r="4.3" fill="none" stroke="#fff" stroke-width="1"/><path d="M3.4 3 L4.2 2.8 L4.6 4 L4.1 4.4 Q4.8 5.6 5.7 6 L6.1 5.5 L7.2 5.9 L7 6.7 Q5 7 3.4 3 Z" fill="#fff"/></svg>0461 238 574
      <span class="sep"></span>
      <svg class="icon" width="8" height="8" viewBox="0 0 10 10"><circle cx="5" cy="5" r="4.3" fill="none" stroke="#fff" stroke-width="1"/><rect x="2.8" y="3.5" width="4.4" height="3" fill="none" stroke="#fff" stroke-width=".8"/><path d="M2.8 3.5 L5 5.2 L7.2 3.5" fill="none" stroke="#fff" stroke-width=".8"/></svg>enquiries@scplumbwork.net.au
    </div>
  </section>

  <!-- Business card, back -->
  <section class="card card-back">
    <div class="wordmark">Silver Creek<br>Plumbing</div>
    <div class="services">Domestic &amp; Commercial Plumbing<span style="margin:0 8px">I</span>Tip Truck &amp; Excavator hire</div>
  </section>

  <!-- Letterhead -->
  <section class="letterhead">
    <svg class="wave" width="668" height="864" viewBox="0 0 668 864">
      <path d="M0 767 Q330 855 668 752 L668 864 L0 864 Z" fill="var(--brand-blue)"/>
      <path d="M0 750 Q250 830 560 792 Q260 824 0 760 Z" fill="var(--swoosh-grey)"/>
    </svg>
    <div class="wordmark">Silver Creek<br>Plumbing</div>

    <div class="letter-body">
      <div class="salutation">Dear Mr. Lorem,</div>
      <p class="para">Lorem ipsum dolor sit amet, consectetuer adipiscing elit, sed diam nonummy nibh euismod tincidunt ut laoreet dolore magna aliquam erat volutpat. Ut wisi enim ad minim veniam, quis nostrud exerci tation ullamcorper suscipit lobortis nisl ut aliquip ex ea commodo consequat. Duis autem vel eum iriure dolor in hendiusto odio dignissim qui blandit praesent luptatum zzril delenit augue duis dolore te feugait nulla facilisi.</p>
      <p class="para">Lorem ipsum dolor sit amet, consectetuer adipiscing elit, sed diam nonummy nibh euismod tincidunt ut laoreet dolore magna aliquam erat volutpat. Ut wisi enim ad minim veniam, quis nostrud exerci tation ullamcorper suscipit lobortis nisl ut aliquip ex ea commodo consequat. Duis autem vel eum iriure dolor in hendiusto odio dignissim qui blandit praesent luptatum zzril delenit augue duis dolore te feugait nulla facilisi.</p>
      <p class="para">Lorem ipsum dolor sit amet, consectetuer adipiscing elit, sed diam nonummy nibh euismod tincidunt ut laoreet dolore magna aliquam erat volutpat. Ut wisi enim ad minim veniam, quis nostrud exerci tation ullamcorper suscipit lobortis nisl ut aliquip ex ea commodo consequat. Duis autem vel eum iriure dolor in hendiusto odio dignissim qui blandit praesent luptatum zzril delenit augue duis dolore te feugait nulla facilisi.</p>
      <div class="closing">Sincerely Your,</div>
      <div class="signature">Your Name</div>
    </div>

    <div class="lh-footer lh-line-1">Domestic &amp; Commercial Plumbing<span class="sep">I</span>Tip Truck &amp; Excavator hire</div>
    <div class="lh-footer lh-line-2">
      <svg class="icon" width="9" height="9" viewBox="0 0 10 10"><circle cx="5" cy="5" r="4.3" fill="none" stroke="#fff" stroke-width="1"/><path d="M3.4 3 L4.2 2.8 L4.6 4 L4.1 4.4 Q4.8 5.6 5.7 6 L6.1 5.5 L7.2 5.9 L7 6.7 Q5 7 3.4 3 Z" fill="#fff"/></svg>0461 238 574<span class="sep">|</span><svg class="icon" width="9" height="9" viewBox="0 0 10 10"><circle cx="5" cy="5" r="4.3" fill="none" stroke="#fff" stroke-width="1"/><rect x="2.8" y="3.5" width="4.4" height="3" fill="none" stroke="#fff" stroke-width=".8"/><path d="M2.8 3.5 L5 5.2 L7.2 3.5" fill="none" stroke="#fff" stroke-width=".8"/></svg>enquiries@scplumbwork.net.au<span class="sep">|</span><b>ABN:</b>&nbsp;47 381 905 462<span class="sep">|</span><b>PCL:</b>&nbsp;5187
    </div>
  </section>

</body>
</html>
```